Demo Screens Needed for Recruiting with AI App

We are in the process of raising money for our startup called PylonGrove. We need demos to show investors what we're trying to do with images. We really love the simplicity and modern look of the Lantern App and want something similar. We will have the "swipe" functionality similar to Kindle as well. The sample images I've attached are only for caregivers but long term this will be for all industries. There will also be a rewards page for loyalty membership. The current landing page is www.pylongrove.example. That will show you the color scheme and logo.

```html
<!DOCTYPE html>
<html lang="en">
<head>
<meta charset="utf-8">
<title>PylonGrove — App Screens</title>
<link href="https://fonts.googleapis.com/css2?family=Outfit:wght@300;400;500;600;700&display=swap" rel="stylesheet">
<style>
:root{
  --canvas:#0d0c22;
  --board-top:#14113a;
  --board-bottom:#0c0b20;
  --phone-top:#1b1350;
  --phone-bottom:#120e34;
  --brand:#2a93c4;
  --brand-bright:#2c9fd3;
  --brand-deep:#2380b3;
  --band:#2f95c4;
  --field:#262a5c;
  --card:#20256a;
  --card-soft:#1c2160;
  --nav:#181c48;
  --white:#ffffff;
  --muted:#b9bde0;
  --dim:#8f93bd;
  --green:#27d36b;
  --gold:#f2a93b;
}
*{box-sizing:border-box;margin:0;padding:0}
html,body{width:1200px;height:2472px;overflow:hidden;background:var(--canvas)}
body{font-family:'Outfit',sans-serif;color:var(--white)}
.board{
  position:absolute;left:0;top:0;width:1251px;height:2576px;
  transform:scale(0.9592);transform-origin:0 0;
  border-radius:60px;overflow:hidden;
  background:radial-gradient(ellipse at 50% 40%,#19164a 0%,var(--board-top) 35%,var(--board-bottom) 100%);
}
.phone{
  position:absolute;width:387px;border-radius:40px;overflow:hidden;
  background:linear-gradient(180deg,var(--phone-top) 0%,var(--phone-bottom) 100%);
}
.phone--welcome{left:219px;top:122px;height:951px}
.phone--login{left:646px;top:122px;height:951px}
.phone--list{left:219px;top:1160px;height:948px;background:linear-gradient(180deg,#1a1450 0%,#15123d 60%,#121030 100%)}
.phone--profile{left:646px;top:1160px;height:1285px;background:linear-gradient(180deg,#1a1450 0%,#15123d 60%,#121030 100%)}
.abs{position:absolute}
.status{position:absolute;left:31px;top:18px;right:22px;height:20px;font-size:15px;font-weight:500}
.status__icons{position:absolute;right:0;top:2px}
.phone--list .status,.phone--profile .status{opacity:.7}

.wordmark{position:absolute;left:0;right:0;top:226px;text-align:center;font-size:46px;font-weight:300;letter-spacing:6px;line-height:1}
.btn{position:absolute;display:flex;align-items:center;justify-content:center;color:var(--white);font-weight:600}
.btn--start{left:19px;top:386px;width:349px;height:65px;border-radius:33px;background:var(--brand-deep);font-size:18px}
.crew-photo{position:absolute;left:9px;top:550px;width:372px;height:230px;border-radius:90px 90px 0 0;background:linear-gradient(180deg,#5a4a48 0%,#9a8070 45%,#d9d2cc 100%);opacity:.9}
.band{position:absolute;left:0;bottom:0;width:387px;height:240px}
.socials{position:absolute;left:0;right:0;top:830px;display:flex;justify-content:center;gap:17px}
.socials span{width:22px;height:22px;border-radius:50%;background:#5f7fd4;opacity:.85}
.socials span:nth-child(2){background:#e0508a}
.socials span:nth-child(3){background:#3c62c9}
.socials span:nth-child(4){background:#6cb8ee}
.copyright{position:absolute;left:0;right:0;top:876px;text-align:center;font-size:12px}
.home-bar{position:absolute;left:127px;width:133px;height:4px;border-radius:2px;background:var(--white)}

.headline{position:absolute;left:22px;top:112px;font-size:38px;font-weight:600;line-height:40px}
.headline__accent{color:var(--brand-bright);font-weight:700}
.lede{position:absolute;left:22px;top:244px;width:190px;font-size:11.5px;line-height:14.5px;color:#dfe1f4}
.field{position:absolute;left:20px;width:347px;height:43px;border-radius:12px;background:var(--field);padding-left:15px;display:flex;align-items:center;font-size:12px;color:#d5d8ef}
.check-row{position:absolute;left:21px;right:23px;top:427px;height:18px;font-size:10px;color:#d5d8ef}
.check{position:absolute;left:0;top:0;width:18px;height:18px;border-radius:4px;background:var(--field)}
.check-row .label{position:absolute;left:25px;top:2px}
.check-row .forgot{position:absolute;right:0;top:2px}
.btn--login{left:21px;top:463px;width:345px;height:42px;border-radius:12px;background:var(--brand-bright);font-size:13.5px;font-weight:500}
.signup{position:absolute;left:0;right:0;top:536px;text-align:center;font-size:12px;padding-left:0}
.signup b{color:var(--brand-bright);font-weight:600}

.topbar{position:absolute;left:18px;right:18px;top:60px;height:46px}
.avatar{position:absolute;border-radius:50%;background:linear-gradient(160deg,#8a7d74,#3c3a4a);border:2px solid #7fc6e6}
.topbar .avatar{left:0;top:0;width:46px;height:46px}
.topbar .user{position:absolute;left:55px;top:12px;font-size:16.5px;font-weight:500}
.bell{position:absolute;right:10px;top:1px;width:44px;height:44px;border-radius:50%;background:#232664;display:flex;align-items:center;justify-content:center}
.bell i{position:absolute;right:6px;top:5px;width:9px;height:9px;border-radius:50%;background:var(--green)}

.title{position:absolute;left:21px;top:126px;font-size:24px;font-weight:500}
.subtitle{position:absolute;left:23px;top:160px;width:270px;font-size:14px;line-height:22px;color:#e3e5f5;font-weight:300}
.chips{position:absolute;left:19px;top:224px;display:flex;gap:6px}
.chip{height:42px;border-radius:21px;background:#242a6c;font-size:12px;font-weight:600;display:flex;align-items:center;justify-content:center}
.carer{position:absolute;left:19px;width:347px;height:82px;border-radius:16px;background:linear-gradient(90deg,#232870,#262a78)}
.carer .avatar{left:18px;top:18px;width:46px;height:46px}
.carer__name{position:absolute;left:75px;top:14px;font-size:16px;font-weight:400}
.carer__meta{position:absolute;left:75px;top:38px;font-size:10px;color:#dfe1f4;display:flex;gap:14px;align-items:center}
.carer__meta em{font-style:normal;display:flex;align-items:center;gap:4px}
.dot{display:inline-block;width:6px;height:6px;border-radius:2px;background:var(--brand-bright)}
.carer__stars{position:absolute;left:75px;top:54px;font-size:9px;letter-spacing:4px;color:var(--brand-bright)}
.carer__stars i{font-style:normal;opacity:.45}
.carer__send{position:absolute;right:28px;top:29px}
.carer--faded{opacity:.28;background:var(--card-soft)}
.nav{position:absolute;left:19px;width:347px;height:62px;border-radius:31px;background:var(--nav);display:flex;justify-content:space-around;align-items:center;padding:0 40px}

.hero-photo{position:absolute;left:19px;top:132px;width:348px;height:388px;border-radius:18px 18px 40px 40px;background:linear-gradient(180deg,#8f8f93 0%,#a88e7a 35%,#5a4b44 70%,#2a2428 100%)}
.action{position:absolute;border-radius:50%;display:flex;align-items:center;justify-content:center}
.action--pass{left:45px;top:482px;width:62px;height:62px;background:#171a3c}
.action--send{left:156px;top:472px;width:74px;height:74px;background:var(--brand-deep);box-shadow:0 0 22px rgba(44,159,211,.7)}
.action--fav{left:279px;top:482px;width:62px;height:62px;background:#171a3c}
.namecard{position:absolute;left:19px;top:563px;width:348px;height:84px;border-radius:16px;background:linear-gradient(90deg,#262c70,#22286a)}
.namecard__name{position:absolute;left:26px;top:32px;font-size:16px}
.namecard__name b{font-weight:600}
.namecard__stars{position:absolute;right:25px;top:31px;color:var(--brand-bright);font-size:15px;letter-spacing:5px}
.details{position:absolute;left:19px;top:668px;width:348px;height:337px;border-radius:16px;background:linear-gradient(180deg,#23297a,#201d6e)}
.detail{position:absolute;left:20px;right:20px;height:46px;display:flex;align-items:center;gap:13px;font-size:12px;border-bottom:1px solid rgba(120,130,220,.25)}
.detail:last-child{border-bottom:none}
.detail svg{flex:0 0 20px}
.about{position:absolute;left:19px;top:1026px;width:348px;height:109px;border-radius:16px;background:#1e2060}
.about h3{position:absolute;left:27px;top:16px;font-size:16px;font-weight:400}
.about p{position:absolute;left:27px;top:41px;width:280px;font-size:7px;line-height:12px;color:#c9cbe6}
.about small{position:absolute;left:27px;top:82px;font-size:6.5px;color:var(--brand-bright)}
</style>
</head>
<body>
<main class="board">

  <!-- Welcome -->
  <section class="phone phone--welcome">
    <div class="status">9:41
      <svg class="status__icons" width="64" height="12" viewBox="0 0 64 12"><g fill="#fff"><rect x="0" y="8" width="3" height="4" rx="1"/><rect x="5" y="6" width="3" height="6" rx="1"/><rect x="10" y="3" width="3" height="9" rx="1"/><rect x="15" y="0" width="3" height="12" rx="1"/><path d="M30 11l-3-3a4 4 0 0 1 6 0z"/><path d="M24 5a9 9 0 0 1 12 0l-1.5 1.5a7 7 0 0 0-9 0z"/><rect x="44" y="2" width="18" height="8" rx="2"/></g></svg>
    </div>
    <div class="wordmark">PYLONGROVE</div>
    <div class="btn btn--start">Get Started</div>
    <div class="crew-photo" role="img" aria-label="Photo of three smiling caregivers standing together"></div>
    <svg class="band" viewBox="0 0 387 240" preserveAspectRatio="none"><path fill="var(--band)" d="M0 2 L8 8 L20 4 L34 14 L52 10 L70 16 L90 9 L110 18 L132 12 L150 16 L172 10 L190 20 L212 16 L236 24 L258 22 L282 32 L300 28 L322 36 L340 32 L362 38 L387 34 L387 240 L0 240Z"/></svg>
    <div class="socials"><span></span><span></span><span></span><span></span></div>
    <div class="copyright">© All rights reserved.</div>
    <div class="home-bar" style="top:917px"></div>
  </section>

  <!-- Login -->
  <section class="phone phone--login">
    <div class="status">9:41
      <svg class="status__icons" width="64" height="12" viewBox="0 0 64 12"><g fill="#fff"><rect x="0" y="8" width="3" height="4" rx="1"/><rect x="5" y="6" width="3" height="6" rx="1"/><rect x="10" y="3" width="3" height="9" rx="1"/><rect x="15" y="0" width="3" height="12" rx="1"/><path d="M30 11l-3-3a4 4 0 0 1 6 0z"/><path d="M24 5a9 9 0 0 1 12 0l-1.5 1.5a7 7 0 0 0-9 0z"/><rect x="44" y="2" width="18" height="8" rx="2"/></g></svg>
    </div>
    <h1 class="headline">Start<br><span class="headline__accent">exploring</span><br>now!</h1>
    <p class="lede">Welcome back! Sign in using your social account or email to continue us</p>
    <div class="field" style="top:312px">Phone Number</div>
    <div class="field" style="top:368px">Password</div>
    <div class="check-row">
      <span class="check"><svg width="18" height="18" viewBox="0 0 18 18"><path d="M5 9l3 3 5-6" fill="none" stroke="#2c9fd3" stroke-width="1.6"/></svg></span>
      <span class="label">Remember me</span>
      <span class="forgot">I forgot my password?</span>
    </div>
    <div class="btn btn--login">Login</div>
    <p class="signup">Still not a member? <b>Sign Up Now</b></p>
    <svg class="band" viewBox="0 0 387 240" preserveAspectRatio="none"><path fill="var(--band)" d="M0 0 L10 8 L24 6 L40 10 L56 8 L74 12 L96 10 L118 16 L136 12 L160 18 L182 14 L206 24 L226 20 L250 30 L272 26 L292 36 L312 30 L336 40 L356 34 L387 38 L387 240 L0 240Z"/></svg>
    <div class="socials"><span></span><span></span><span></span><span></span></div>
    <div class="copyright">© All rights reserved.</div>
    <div class="home-bar" style="top:917px"></div>
  </section>

  <!-- Find your tribe -->
  <section class="phone phone--list">
    <div class="status">9:41
      <svg class="status__icons" width="64" height="12" viewBox="0 0 64 12"><g fill="#fff"><rect x="0" y="8" width="3" height="4" rx="1"/><rect x="5" y="6" width="3" height="6" rx="1"/><rect x="10" y="3" width="3" height="9" rx="1"/><rect x="15" y="0" width="3" height="12" rx="1"/><path d="M30 11l-3-3a4 4 0 0 1 6 0z"/><path d="M24 5a9 9 0 0 1 12 0l-1.5 1.5a7 7 0 0 0-9 0z"/><rect x="44" y="2" width="18" height="8" rx="2"/></g></svg>
    </div>
    <div class="topbar">
      <div class="avatar" role="img" aria-label="User profile photo"></div>
      <div class="user">User Name</div>
      <div class="bell"><svg width="22" height="22" viewBox="0 0 24 24" fill="none" stroke="#fff" stroke-width="1.6"><path d="M6 17V11a6 6 0 0 1 12 0v6l2 2H4z"/><path d="M10 21h4"/></svg><i></i></div>
    </div>
    <h2 class="title">Find Your Tribe</h2>
    <p class="subtitle">Please enter the features of the caregiver you need from the filter below.</p>
    <div class="chips">
      <div class="chip" style="width:112px">Palo Alto - 15 mi</div>
      <div class="chip" style="width:52px">Date</div>
      <div class="chip" style="width:83px">$25 / hr</div>
      <div class="chip" style="width:84px">More Filters</div>
    </div>

    <article class="carer" style="top:290px">
      <div class="avatar" role="img" aria-label="Caregiver photo"></div>
      <div class="carer__name">Rowan M.</div>
      <div class="carer__meta"><em><span class="dot"></span>Palo Alto, CA</em><em><span class="dot"></span>$25</em></div>
      <div class="carer__stars">★★★★<i>★</i></div>
      <svg class="carer__send" width="24" height="24" viewBox="0 0 24 24"><path d="M22 2L2 10l8 3 3 9z" fill="var(--brand-bright)"/></svg>
    </article>
    <article class="carer" style="top:393px">
      <div class="avatar" role="img" aria-label="Caregiver photo"></div>
      <div class="carer__name">Rowan M.</div>
      <div class="carer__meta"><em><span class="dot"></span>Palo Alto, CA</em><em><span class="dot"></span>$25</em></div>
      <div class="carer__stars">★★★★<i>★</i></div>
      <svg class="carer__send" width="24" height="24" viewBox="0 0 24 24"><path d="M22 2L2 10l8 3 3 9z" fill="var(--brand-bright)"/></svg>
    </article>
    <article class="carer" style="top:497px">
      <div class="avatar" role="img" aria-label="Caregiver photo"></div>
      <div class="carer__name">Mara B.</div>
      <div class="carer__meta"><em><span class="dot"></span>Palo Alto, CA</em><em><span class="dot"></span>$25</em></div>
      <div class="carer__stars">★★★★<i>★</i></div>
      <svg class="carer__send" width="24" height="24" viewBox="0 0 24 24"><path d="M22 2L2 10l8 3 3 9z" fill="var(--brand-bright)"/></svg>
    </article>
    <article class="carer" style="top:601px">
      <div class="avatar" role="img" aria-label="Caregiver photo"></div>
      <div class="carer__name">Iris V.</div>
      <div class="carer__meta"><em><span class="dot"></span>Palo Alto, CA</em><em><span class="dot"></span>$25</em></div>
      <div class="carer__stars">★★★★<i>★</i></div>
      <svg class="carer__send" width="24" height="24" viewBox="0 0 24 24"><path d="M22 2L2 10l8 3 3 9z" fill="var(--brand-bright)"/></svg>
    </article>
    <article class="carer carer--faded" style="top:705px">
      <div class="avatar" role="img" aria-label="Caregiver photo"></div>
      <div class="carer__name">Nadia B.</div>
      <div class="carer__meta"><em><span class="dot"></span>Palo Alto, CA</em><em><span class="dot"></span>$25</em></div>
      <div class="carer__stars">★★★★<i>★</i></div>
      <svg class="carer__send" width="24" height="24" viewBox="0 0 24 24"><path d="M22 2L2 10l8 3 3 9z" fill="var(--brand-bright)"/></svg>
    </article>

    <nav class="nav" style="top:822px">
      <svg width="22" height="22" viewBox="0 0 24 24"><path d="M3 11l9-8 9 8v9a2 2 0 0 1-2 2H5a2 2 0 0 1-2-2z" fill="var(--brand-bright)"/></svg>
      <svg width="20" height="20" viewBox="0 0 24 24"><path d="M12 2a8 8 0 0 0-8 8c0 6 8 12 8 12s8-6 8-12a8 8 0 0 0-8-8zm0 11a3 3 0 1 1 0-6 3 3 0 0 1 0 6z" fill="#fff"/></svg>
      <svg width="20" height="20" viewBox="0 0 24 24"><path d="M12 21l-9-9a5 5 0 0 1 9-6 5 5 0 0 1 9 6z" fill="#fff"/></svg>
      <svg width="20" height="20" viewBox="0 0 24 24"><path d="M12 3a9 9 0 0 0-8 13l-1 5 5-1a9 9 0 1 0 4-17z" fill="#fff"/><path d="M8 10h8M8 14h5" stroke="#181c48" stroke-width="2"/></svg>
    </nav>
    <div class="home-bar" style="top:916px"></div>
  </section>

  <!-- Profile -->
  <section class="phone phone--profile">
    <div class="status">9:41
      <svg class="status__icons" width="64" height="12" viewBox="0 0 64 12"><g fill="#fff"><rect x="0" y="8" width="3" height="4" rx="1"/><rect x="5" y="6" width="3" height="6" rx="1"/><rect x="10" y="3" width="3" height="9" rx="1"/><rect x="15" y="0" width="3" height="12" rx="1"/><path d="M30 11l-3-3a4 4 0 0 1 6 0z"/><path d="M24 5a9 9 0 0 1 12 0l-1.5 1.5a7 7 0 0 0-9 0z"/><rect x="44" y="2" width="18" height="8" rx="2"/></g></svg>
    </div>
    <div class="topbar">
      <div class="avatar" role="img" aria-label="User profile photo"></div>
      <div class="user">User Name</div>
      <div class="bell"><svg width="22" height="22" viewBox="0 0 24 24" fill="none" stroke="#fff" stroke-width="1.6"><path d="M6 17V11a6 6 0 0 1 12 0v6l2 2H4z"/><path d="M10 21h4"/></svg><i></i></div>
    </div>
    <div class="hero-photo" role="img" aria-label="Portrait photo of a smiling caregiver wearing a hat outdoors"></div>
    <div class="action action--pass"><svg width="26" height="26" viewBox="0 0 24 24"><path d="M5 5l14 14M19 5L5 19" stroke="#fff" stroke-width="3" stroke-linecap="round"/></svg></div>
    <div class="action action--send"><svg width="36" height="36" viewBox="0 0 24 24"><path d="M22 2L2 10l8 3 3 9z" fill="#fff"/></svg></div>
    <div class="action action--fav"><svg width="28" height="28" viewBox="0 0 24 24"><path d="M12 2l3 6.5 7 .8-5.2 4.8 1.4 7L12 17.5 5.8 21l1.4-7L2 9.3l7-.8z" fill="var(--gold)"/></svg></div>

    <div class="namecard">
      <div class="namecard__name">Tessa Lane, <b>23</b></div>
      <div class="namecard__stars">★★★★★</div>
    </div>

    <div class="details">
      <div class="detail" style="top:8px"><svg width="20" height="20" viewBox="0 0 24 24" fill="none" stroke="var(--brand-bright)" stroke-width="1.8"><circle cx="6" cy="6" r="3"/><circle cx="18" cy="18" r="3"/><path d="M9 6h6a3 3 0 0 1 0 6H9a3 3 0 0 0 0 6h6"/></svg>Palo Alto, CA</div>
      <div class="detail" style="top:54px"><svg width="20" height="20" viewBox="0 0 24 24"><path d="M3 4h18v12H9l-5 4v-4H3z" fill="var(--brand-bright)"/></svg>English, Spanish, Mandarin</div>
      <div class="detail" style="top:101px"><svg width="20" height="20" viewBox="0 0 24 24" fill="none" stroke="var(--brand-bright)" stroke-width="1.8"><rect x="3" y="4" width="18" height="16" rx="2"/><path d="M7 9h10M7 13h10M7 17h6"/></svg>Bachelor's Degree</div>
      <div class="detail" style="top:147px"><svg width="20" height="20" viewBox="0 0 24 24"><ellipse cx="8" cy="13" rx="4" ry="7" fill="var(--brand-bright)"/><ellipse cx="17" cy="10" rx="4" ry="7" fill="var(--brand-bright)"/></svg>Age Groups: 0 - 11 mo, 1 - 3 yrs, 4 - 5 yrs</div>
      <div class="detail" style="top:193px"><svg width="20" height="20" viewBox="0 0 24 24"><rect x="3" y="7" width="18" height="13" rx="2" fill="var(--brand-bright)"/><path d="M9 7V4h6v3" stroke="var(--brand-bright)" stroke-width="2" fill="none"/></svg>CPR Trained Special Needs Care</div>
      <div class="detail" style="top:240px"><svg width="20" height="20" viewBox="0 0 24 24" fill="none" stroke="var(--brand-bright)" stroke-width="1.8"><circle cx="12" cy="13" r="8"/><path d="M12 9v4l2 2M10 3h4"/></svg>Full - time, open to part - time</div>
      <div class="detail" style="top:287px"><svg width="20" height="20" viewBox="0 0 24 24"><path d="M12 21l-9-9a5 5 0 0 1 9-6 5 5 0 0 1 9 6z" fill="var(--brand-bright)"/><path d="M5 12h4l2-3 2 5 2-2h4" stroke="#201d6e" stroke-width="1.6" fill="none"/></svg>Comfortable with pets, Meal Prep</div>
    </div>

    <div class="about">
      <h3>About</h3>
      <p>She is a warm and steady caregiver who plans calm routines, keeps little ones safe and sends clear notes to parents after every visit.</p>
      <small>VIEW ALL</small>
    </div>

    <nav class="nav" style="top:1163px">
      <svg width="22" height="22" viewBox="0 0 24 24"><path d="M3 11l9-8 9 8v9a2 2 0 0 1-2 2H5a2 2 0 0 1-2-2z" fill="var(--brand-bright)"/></svg>
      <svg width="20" height="20" viewBox="0 0 24 24"><path d="M12 2a8 8 0 0 0-8 8c0 6 8 12 8 12s8-6 8-12a8 8 0 0 0-8-8zm0 11a3 3 0 1 1 0-6 3 3 0 0 1 0 6z" fill="#fff"/></svg>
      <svg width="20" height="20" viewBox="0 0 24 24"><path d="M12 21l-9-9a5 5 0 0 1 9-6 5 5 0 0 1 9 6z" fill="#fff"/></svg>
      <svg width="20" height="20" viewBox="0 0 24 24"><path d="M12 3a9 9 0 0 0-8 13l-1 5 5-1a9 9 0 1 0 4-17z" fill="#fff"/><path d="M8 10h8M8 14h5" stroke="#181c48" stroke-width="2"/></svg>
    </nav>
    <div class="home-bar" style="top:1257px"></div>
  </section>

</main>
</body>
</html>
```